Private Medical Clinic needs a letterhead design

Letterhead that can be edited. Letter head is needed for printing official doctor's notes, referrals, etc in a medical clinic. The letterhead should use the attached logos

```html
<!DOCTYPE html>
<html lang="en">
<head>
<meta charset="utf-8">
<title>Quiet Meadow Family Medicine – Stationery</title>
<link rel="stylesheet" href="https://fonts.googleapis.com/css2?family=EB+Garamond:wght@400&family=Montserrat:wght@400;600&display=swap">
<style>
  :root {
    --backdrop: #efefef;
    --olive: #41443a;
    --paper: #ffffff;
    --ink-light: #f2f2ee;
    --bloom-dark: #6d775f;
    --bloom-light: #e4e4e4;
    --serif: "EB Garamond", Georgia, serif;
    --sans: "Montserrat", Arial, sans-serif;
  }
  * { margin: 0; padding: 0; box-sizing: border-box; }
  html, body { width: 1200px; height: 687px; overflow: hidden; background: var(--backdrop); }
  .canvas { position: relative; width: 1200px; height: 687px; }

  .sheet { position: absolute; top: 73px; width: 406px; height: 574px; }

  /* Cover sheet */
  .cover { left: 175px; background: var(--olive); }
  .cover .brand { position: absolute; right: 37px; top: 140px; text-align: left; color: var(--ink-light); font-family: var(--serif); font-weight: 400; }
  .cover .brand-name { font-size: 36px; line-height: 1; letter-spacing: -0.3px; }
  .cover .brand-line { font-size: 9px; letter-spacing: 1.6px; margin-top: 8px; margin-left: 3px; text-transform: uppercase; }
  .cover .bloom { position: absolute; left: 0; top: 290px; width: 278px; height: 284px;
    background: radial-gradient(ellipse 55% 45% at 42% 42%, rgba(109,119,95,.55), rgba(109,119,95,.15) 70%, rgba(65,68,58,0) 100%); }
  .cover .tagline { position: absolute; right: 37px; bottom: 36px; color: var(--ink-light); font-family: var(--serif); font-size: 13px; letter-spacing: .2px; }

  /* Letterhead sheet */
  .letterhead { left: 625px; background: var(--paper); box-shadow: 0 1px 3px rgba(0,0,0,.08); }
  .letterhead .band { position: absolute; left: 0; right: 0; top: 14px; height: 92px; background: var(--olive); }
  .letterhead .brand { position: absolute; left: 30px; top: 35px; color: var(--ink-light); font-family: var(--serif); }
  .letterhead .brand-name { font-size: 24px; line-height: 1; }
  .letterhead .brand-line { font-size: 6px; letter-spacing: 1.2px; margin-top: 5px; margin-left: 2px; text-transform: uppercase; }
  .contact { position: absolute; left: 274px; top: 33px; list-style: none; color: var(--ink-light); font-family: var(--sans); font-size: 6px; line-height: 1.5; }
  .contact li { display: flex; align-items: flex-start; gap: 5px; margin-bottom: 3px; }
  .contact svg { width: 6px; height: 6px; margin-top: 1px; flex: none; }
  .contact strong { font-weight: 600; }
  .letterhead .bloom { position: absolute; right: 0; bottom: 0; width: 270px; height: 287px;
    background: radial-gradient(ellipse 45% 38% at 45% 35%, rgba(215,215,215,.7), rgba(228,228,228,.25) 70%, rgba(255,255,255,0) 100%); }
</style>
</head>
<body>
<main class="canvas">
  <section class="sheet cover">
    <div class="brand">
      <div class="brand-name">Quiet Meadow</div>
      <div class="brand-line">Family Medicine</div>
    </div>
    <div class="bloom" role="img" aria-label="Faint illustration of a dandelion seed head releasing seeds into the wind"></div>
    <p class="tagline">HEALING THE WHOLE PERSON</p>
  </section>

  <section class="sheet letterhead">
    <header class="band">
      <div class="brand">
        <div class="brand-name">Quiet Meadow</div>
        <div class="brand-line">Family Medicine</div>
      </div>
      <ul class="contact">
        <li><svg viewBox="0 0 10 10" fill="none" stroke="currentColor" stroke-width="1"><path d="M2 1l2 2-1 1.2c.6 1.3 1.5 2.2 2.8 2.8L7 6l2 2-1.2 1.2C4.5 9 1 5.5.8 2.2z"/></svg><span>555.014.2290</span></li>
        <li><svg viewBox="0 0 10 10" fill="none" stroke="currentColor" stroke-width="1"><rect x="1" y="2" width="8" height="6"/><path d="M1 2l4 3.5L9 2"/></svg><span>info@quietmeadow.com</span></li>
        <li><svg viewBox="0 0 10 10" fill="none" stroke="currentColor" stroke-width="1"><path d="M5 9.5S1.8 6 1.8 4a3.2 3.2 0 016.4 0C8.2 6 5 9.5 5 9.5z"/><circle cx="5" cy="4" r="1.1"/></svg><span>420 Linden Row, Suite 110B<br>Ashford, FL 32000</span></li>
        <li><svg viewBox="0 0 10 10" fill="none" stroke="currentColor" stroke-width="1"><circle cx="5" cy="5" r="4"/><path d="M1 5h8M5 1c-2 2.5-2 5.5 0 8M5 1c2 2.5 2 5.5 0 8"/></svg><span>www.<strong>QUIETMEADOW</strong>.com</span></li>
      </ul>
    </header>
    <div class="bloom" role="img" aria-label="Faint watermark illustration of two dandelions with seeds drifting away"></div>
  </section>
</main>
</body>
</html>
```